Healthcare IT firm needs classy and unique business care design

We need a business card design that incorporates our new logo design (attached) Prefer a purple based designed. I would really love to see something utilizing the "3D" version of the logo (purple on the reflective wall). I want something a little more than my logo printed along with a person's detailed contact information.
Contact Information for Business Card
Want something polished, professional, and a little unique in the design.
Colors
6b449b
Requirements
Must have
- Please use similar font as the logo design
Nice to have
- Would like to see the 3d version of my logo incorporated into the design.

```html
<!DOCTYPE html>
<html lang="en">
<head>
<meta charset="utf-8">
<title>Veranda Health Systems – Business Card</title>
<link rel="stylesheet" href="https://fonts.googleapis.com/css2?family=Roboto:wght@400;700&display=swap">
<style>
  :root{
    --stage:#2e2e2e;
    --card-dark:#0b0b0b;
    --card-light:#ffffff;
    --purple:#6b449b;
    --ink:#2a2a2a;
    --white:#ffffff;
  }
  *{box-sizing:border-box;margin:0;padding:0}
  html,body{width:1200px;height:896px;overflow:hidden}
  body{
    background:var(--stage);
    font-family:"Roboto",Arial,sans-serif;
    position:relative;
  }
  .card{
    position:absolute;
    top:293px;
    width:540px;
    height:310px;
    border-radius:20px;
  }
  .card--back{left:40px;background:var(--card-dark);box-shadow:0 10px 30px rgba(0,0,0,.5)}
  .card--front{left:620px;background:var(--card-light);box-shadow:0 10px 30px rgba(0,0,0,.5)}

  .brand{
    position:absolute;
    display:flex;
    align-items:center;
    gap:12px;
    font-weight:700;
    white-space:nowrap;
  }
  .brand__mark{display:block;flex:none}
  .card--back .brand{left:50%;top:118px;transform:translateX(-50%);color:var(--white);font-size:34px}
  .card--back .brand__mark{width:22px;height:22px;background:var(--white)}
  .card--back .website{
    position:absolute;left:0;right:0;top:210px;text-align:center;
    color:var(--white);font-size:14px;letter-spacing:.5px;
  }

  .card--front .brand{right:34px;top:36px;color:var(--purple);font-size:26px}
  .card--front .brand__mark{width:17px;height:17px;background:var(--purple)}

  .contact{position:absolute;left:36px;bottom:32px}
  .contact__name{color:var(--purple);font-weight:700;font-size:22px;line-height:1.1}
  .contact__role{color:var(--ink);font-size:14px;margin:3px 0 10px}
  .contact__list{list-style:none;color:var(--ink);font-size:14px;line-height:1.5}
  .contact__list li{display:flex;align-items:center;gap:8px}
  .contact__list svg{width:11px;height:11px;fill:var(--purple);flex:none}
  .contact__list .indent{padding-left:19px}
  .accent{color:var(--purple)}
</style>
</head>
<body>
  <section class="card card--back">
    <div class="brand"><span class="brand__mark"></span>Veranda Health Systems</div>
    <p class="website">www.verandahealth.com</p>
  </section>

  <section class="card card--front">
    <div class="brand"><span class="brand__mark"></span>Veranda Health Systems</div>
    <div class="contact">
      <h1 class="contact__name">Daniel Reyes</h1>
      <p class="contact__role">Founder</p>
      <ul class="contact__list">
        <li><svg viewBox="0 0 24 24" aria-hidden="true"><path d="M6.6 10.8a15 15 0 0 0 6.6 6.6l2.2-2.2a1 1 0 0 1 1-.25 11.4 11.4 0 0 0 3.6.57 1 1 0 0 1 1 1V20a1 1 0 0 1-1 1A17 17 0 0 1 3 4a1 1 0 0 1 1-1h3.5a1 1 0 0 1 1 1c0 1.25.2 2.45.57 3.57a1 1 0 0 1-.25 1z"/></svg>555-014-2286</li>
        <li><svg viewBox="0 0 24 24" aria-hidden="true"><path d="M2 5h20v14H2zm2 2v.5l8 5 8-5V7zm0 2.8V17h16V9.8l-8 5z"/></svg>hello@verandahealth.com</li>
        <li><svg viewBox="0 0 24 24" aria-hidden="true"><circle cx="12" cy="12" r="10"/></svg>www.<span class="accent">verandahealth</span>.com</li>
        <li class="indent">482 Harbor Point Rd.</li>
        <li class="indent">Coral Bay, FL 33000</li>
      </ul>
    </div>
  </section>
</body>
</html>
```